CASH PAYMENT DISCOUNT NOTICE POSTED IN CASH REGISTER AREA

LOOKING TO MAKE A FLYER OR A POSTED NOTICE FOR CUSTOMERS PAYING FOR OVER-THE-COUNTER MERCHANDISE AND WHO PAY BY CASH METHOD TO GET A 4% CASH DISCOUNT.
PRESCRIPTIONS ARE EXCLUDED FROM THIS CASH DISCOUNT.

Target Market(s)

RETAIL CUSTOMERS

Industry/Entity Type

RETAIL PHARMACY

Colors
0054AA
0677BA
7BADD7
CADEEF
E8F1F8
EB3D1F
EC4F4E
F09395
F8D3D4
FCEDEE

Requirements
Must have
• LOGO COLORS
Nice to have
• EYE CATCHING

```html
<!DOCTYPE html>
<html lang="en">
<head>
<meta charset="utf-8">
<title>Cash Discount Notice – Harlow Pharmacy</title>
<link href="https://fonts.googleapis.com/css2?family=Anton&family=Montserrat:wght@600;700;900&family=Poppins:ital,wght@1,700&display=swap" rel="stylesheet">
<style>
  :root {
    --page-bg: #e8ebef;
    --blue-deep: #0a3a9e;
    --blue-brand: #0054AA;
    --blue-mid: #0677BA;
    --blue-bright: #1a8cf2;
    --blue-soft: #7BADD7;
    --blue-pale: #CADEEF;
    --blue-mist: #E8F1F8;
    --red-brand: #EB3D1F;
    --red-deep: #b01d22;
    --orange: #f15a24;
    --white: #ffffff;
    --ticket-a: #2fb4f5;
    --ticket-b: #2a63f0;
  }
  * { box-sizing: border-box; margin: 0; padding: 0; }
  html, body {
    width: 1200px; height: 1200px; overflow: hidden;
    background: var(--page-bg);
  }
  .notice {
    position: absolute; left: 160px; top: 30px;
    width: 880px; height: 1140px; overflow: hidden;
    background:
      radial-gradient(ellipse 420px 360px at 440px 200px, rgba(202,222,239,0.75), rgba(123,173,215,0) 70%),
      linear-gradient(180deg, var(--blue-bright) 0%, #0b6fe0 40%, var(--blue-brand) 75%, var(--blue-deep) 100%);
    font-family: "Montserrat", sans-serif;
    color: var(--white);
  }
  .notice__art { position: absolute; inset: 0; }
  .ticket { position: absolute; border-radius: 14px; background: linear-gradient(135deg, var(--ticket-a), var(--ticket-b)); }
  .ticket--blur { filter: blur(5px); opacity: 0.9; }
  .brand-tab { position: absolute; left: 0; top: 0; width: 880px; height: 140px; }
  .brand-name {
    position: absolute; left: 0; right: 0; top: 42px;
    display: flex; align-items: center; justify-content: center; gap: 12px;
    font-family: "Montserrat", sans-serif; font-weight: 700; font-size: 30px;
    color: var(--blue-brand); letter-spacing: 1px; white-space: nowrap;
  }
  .brand-name__dot { width: 22px; height: 22px; border-radius: 50%; background: var(--red-brand); }
  .headline-lead {
    position: absolute; left: 164px; top: 202px; width: 553px; height: 74px;
    border: 3px solid var(--white); border-radius: 14px;
    display: flex; align-items: center; justify-content: center;
    font-weight: 700; font-size: 50px; letter-spacing: 1px; line-height: 1;
    white-space: nowrap;
    text-shadow: 0 3px 6px rgba(0,0,0,0.25);
  }
  .headline-big { position: absolute; left: 0; top: 0; width: 880px; height: 940px; overflow: visible; }
  .disclaimer {
    position: absolute; left: 0; right: 0; top: 930px; text-align: center;
    font-family: "Poppins", sans-serif; font-style: italic; font-weight: 700;
    font-size: 20.5px; letter-spacing: 0.2px; white-space: nowrap;
  }
  .disclaimer-rule { position: absolute; left: 104px; width: 672px; top: 965px; height: 1px; background: rgba(232,241,248,0.5); }
  .website {
    position: absolute; left: 0; right: 0; top: 1035px; text-align: center;
    font-weight: 700; font-size: 24px; letter-spacing: 1.5px; white-space: nowrap;
  }
  .socials {
    position: absolute; left: 0; right: 0; top: 1088px;
    display: flex; justify-content: center; gap: 40px;
  }
  .social { display: flex; align-items: center; gap: 14px; font-weight: 600; font-size: 12px; letter-spacing: 1.8px; white-space: nowrap; }
  .social__mark { width: 24px; height: 24px; border-radius: 5px; background: var(--ticket-a); }
</style>
</head>
<body>
<main class="notice">
  <div class="notice__art" role="img" aria-label="Floating discount coupon tickets">
    <div class="ticket" style="left:800px;top:130px;width:110px;height:80px;transform:rotate(-40deg);"></div>
    <div class="ticket ticket--blur" style="left:-20px;top:280px;width:150px;height:110px;transform:rotate(-5deg);"></div>
    <div class="ticket ticket--blur" style="left:815px;top:440px;width:80px;height:40px;transform:rotate(-12deg);"></div>
    <div class="ticket" style="left:108px;top:595px;width:48px;height:58px;transform:rotate(-20deg);"></div>
    <div class="ticket" style="left:700px;top:614px;width:58px;height:36px;transform:rotate(-15deg);"></div>
    <div class="ticket" style="left:-30px;top:1040px;width:150px;height:110px;transform:rotate(-40deg);"></div>
    <div class="ticket ticket--blur" style="left:760px;top:1000px;width:150px;height:120px;transform:rotate(35deg);"></div>
  </div>

  <svg class="brand-tab" viewBox="0 0 880 140" aria-hidden="true">
    <path d="M199 0 L682 0 L603 116 Q592 132 570 132 L310 132 Q288 132 277 116 Z" fill="#ffffff"/>
  </svg>
  <div class="brand-name"><span class="brand-name__dot"></span>Harlow Pharmacy</div>

  <div class="headline-lead">PAY CASH TO GET</div>

  <svg class="headline-big" viewBox="0 0 880 940">
    <defs>
      <linearGradient id="redFill" x1="0" y1="0" x2="0" y2="1">
        <stop offset="0" stop-color="#b01d22"/>
        <stop offset="1" stop-color="#f15a24"/>
      </linearGradient>
      <linearGradient id="blueFill" x1="0" y1="0" x2="0" y2="1">
        <stop offset="0" stop-color="#0677e0"/>
        <stop offset="1" stop-color="#0a3a9e"/>
      </linearGradient>
    </defs>
    <text x="440" y="534" text-anchor="middle" textLength="400" lengthAdjust="spacingAndGlyphs"
          font-family="Montserrat, sans-serif" font-weight="900" font-size="285"
          fill="url(#redFill)" stroke="#ffffff" stroke-width="16" stroke-linejoin="round" paint-order="stroke">4%</text>
    <text x="433" y="718" text-anchor="middle" textLength="350" lengthAdjust="spacingAndGlyphs"
          font-family="Anton, sans-serif" font-size="150"
          fill="url(#blueFill)" stroke="#ffffff" stroke-width="14" stroke-linejoin="round" paint-order="stroke">CASH</text>
    <text x="437" y="884" text-anchor="middle" textLength="670" lengthAdjust="spacingAndGlyphs"
          font-family="Anton, sans-serif" font-size="162"
          fill="url(#blueFill)" stroke="#ffffff" stroke-width="14" stroke-linejoin="round" paint-order="stroke">DISCOUNT</text>
  </svg>

  <p class="disclaimer">*PRESCRIPTIONS ARE EXCLUDED FROM THIS CASH DISCOUNT*</p>
  <div class="disclaimer-rule"></div>

  <p class="website">www.yourcompany.website.com</p>

  <div class="socials">
    <div class="social"><span class="social__mark"></span>YOURCOMPANY</div>
    <div class="social"><span class="social__mark"></span>YOURCOMPANY</div>
    <div class="social"><span class="social__mark"></span>YOURCOMPANY</div>
  </div>
</main>
</body>
</html>
```